Cocktail Bar Aperitivo Promotion

I need a flyer designed for my aperitivo promotion. Aperitivo is an Italian tradition much like the cocktail hour where you can relax and unwind over a drink and a little snack.
Bramble Toots a unique and fun 1950’s style bar - a relaxed local meeting place, the kind of bar where your bartender drinks on their night off. The final design should reflect the enthusiastic spirit of the 1950s cocktail culture as well as the fun, summery Italian vibe of the aperitvo and it needs to highlight the 2 aperitivo cocktails on offer, their price and the time of the promotion. Please also include the logo, address, phone number and website.
Negronis $16
Vellaro Spritz $14
All share plates $10
From 4pm - 6pm every day
Address: 472 Wexcombe Rd Wexcombe
Phone: 8153 2947
brambletoots.com.au
Please also refer to our website- brambletoots.com.au for a sense of who we are and what we do.

```html
<!DOCTYPE html>
<html lang="en">
<head>
<meta charset="utf-8">
<title>Bramble Toots – Aperitivo Offer</title>
<link rel="stylesheet" href="https://fonts.googleapis.com/css2?family=Yellowtail&family=Gochi+Hand&family=Josefin+Sans:wght@400;600;700&display=swap">
<style>
  :root {
    --backdrop: #e9e4dd;
    --brick-light: #d9825f;
    --brick-mid: #b95a3f;
    --brick-dark: #8e3b2a;
    --panel: #ffffff;
    --ink: #2a2624;
    --chalk-board: #262424;
    --chalk: #f4f1ec;
    --cream: #f6dca6;
    --dash: #6d6762;
    --icon-fill: rgba(255,255,255,0.88);
  }
  * { box-sizing: border-box; margin: 0; padding: 0; }
  html, body {
    width: 1200px; height: 1023px; overflow: hidden;
    background: var(--backdrop);
  }
  .canvas {
    position: relative; width: 1200px; height: 1023px;
    display: flex; align-items: center; justify-content: center;
  }
  .flyer {
    position: relative; width: 520px; height: 910px; overflow: hidden;
    box-shadow: 0 6px 24px rgba(0,0,0,0.18);
  }
  .brick-wall {
    position: absolute; inset: 0;
    background: linear-gradient(160deg, var(--brick-light) 0%, var(--brick-mid) 55%, var(--brick-dark) 100%);
  }
  .offer-panel {
    position: absolute; left: 38px; right: 38px; top: 92px; height: 660px;
    background: var(--panel);
  }
  .offer-panel::after {
    content: ""; position: absolute; inset: 8px;
    border: 1.5px dashed var(--dash);
  }
  .brand-badge {
    position: absolute; left: 250px; top: 40px;
    width: 190px; height: 190px; border-radius: 50%;
    background: var(--cream);
    display: flex; align-items: center; justify-content: center;
    z-index: 2;
  }
  .brand-name {
    font-family: "Josefin Sans", sans-serif; font-weight: 700;
    font-size: 30px; line-height: 1.05; color: var(--ink);
    text-align: center; text-transform: uppercase;
  }
  .offer-title {
    position: absolute; left: 0; right: 0; top: 238px; z-index: 2;
    font-family: "Yellowtail", cursive; font-size: 66px;
    color: var(--ink); text-align: center;
  }
  .offer-hours {
    position: absolute; left: 60px; right: 60px; top: 335px; z-index: 2;
    display: flex; align-items: center; gap: 12px;
    font-family: "Josefin Sans", sans-serif; font-weight: 600;
    font-size: 17px; letter-spacing: 1.5px; color: var(--ink);
    text-transform: uppercase; white-space: nowrap;
  }
  .offer-hours .rule { flex: 1; height: 6px; border-top: 1.5px solid var(--ink); border-bottom: 1.5px solid var(--ink); }
  .chalk-band {
    position: absolute; left: 0; right: 0; top: 375px; height: 200px;
    background: var(--chalk-board); z-index: 2;
    padding: 22px 0 0 120px;
  }
  .menu-item {
    font-family: "Gochi Hand", cursive; font-size: 40px; line-height: 56px;
    color: var(--chalk); display: flex; gap: 28px;
  }
  .venue-details {
    position: absolute; left: 0; right: 0; top: 612px; z-index: 2;
    font-family: "Josefin Sans", sans-serif; font-size: 17px; line-height: 28px;
    color: var(--ink); text-align: center;
  }
  .social-row {
    position: absolute; left: 0; right: 0; top: 800px;
    display: flex; justify-content: center; gap: 18px;
  }
  .social-dot { width: 44px; height: 44px; border-radius: 50%; background: var(--icon-fill); }
</style>
</head>
<body>
<main class="canvas">
  <article class="flyer">
    <div class="brick-wall" role="img" aria-label="Red and cream brick wall texture"></div>
    <section class="offer-panel"></section>
    <div class="brand-badge"><span class="brand-name">Bramble<br>Toots</span></div>
    <h1 class="offer-title">Aperitivo Offer</h1>
    <p class="offer-hours"><span class="rule"></span>From 4pm – 6pm every day<span class="rule"></span></p>
    <section class="chalk-band">
      <p class="menu-item"><span>Negronis</span><span>$16</span></p>
      <p class="menu-item"><span>Vellaro Spritz</span><span>$14</span></p>
      <p class="menu-item"><span>All share plates</span><span>$10</span></p>
    </section>
    <address class="venue-details" style="font-style:normal">
      472 Wexcombe Rd Wexcombe<br>
      8153 2947<br>
      brambletoots.com.au
    </address>
    <div class="social-row">
      <span class="social-dot"></span><span class="social-dot"></span><span class="social-dot"></span>
      <span class="social-dot"></span><span class="social-dot"></span><span class="social-dot"></span>
      <span class="social-dot"></span>
    </div>
  </article>
</main>
</body>
</html>
```